External Window Signage Design – Antiaging Center

I would like to dress our shop windows in order to promote our activities in medical aesthetics, meso-aesthetics, anti-ageing care and classical beauty. In fact, our 350 m² center is located on the first floor of a building where there is a lot of traffic, as well as a bus stop and metro station. And right in front of a twenty-floor building of the Northern Tariff Bureau.
We want to communicate our activities to our customers with photos and text in a storefront window. So that they can what we do and visit our website www.lumivora.be (our site is in French) as well as our social networks, like picturegram, chatterbook,…
We'd like a window signage : Elegant, Modern, New, Pure, Clean
We are located on the corners of a building, where we have 8 windows on one side and 10 windows on the other, the dimensions are :
Windows
• Height: 125 cm
• Width: 130 cm
Small windows
• Height: 134 cm
• Width: 40 cm
I would say let your imagination go free. I will have other projects for the winner.
Don't hesitate to ask me if you need other formats of the logo or color, like white.
Updates

https://www.pixelbazaar-example.com/design/58204917, I'D LIKE TO HAVE A PROJECT LIKE THIS IF POSSIBLE WITH THE LITTLE WINDOW UNDERNEATH AS WELL.

Target Market(s)

People who want to take care of their external appearance, look beautiful and good looking, womens/girls - mens/boys

Requirements
Must have
• Face and silhouette of a woman. Elegant
Serious, Modern, Professional, Feminine,Upmarket
Nice to have
• To put the different treatments that we propose,
Should not have
• We absolutely don't want a classic beauty center signage, which is reviewed many times

```html
<!DOCTYPE html>
<html lang="en">
<head>
<meta charset="utf-8">
<title>Lumivora – Window Signage</title>
<link rel="stylesheet" href="https://fonts.googleapis.com/css2?family=Inter:wght@300;400;500;800&display=swap">
<style>
  :root{
    --red:#c8102e;
    --gold:#b89c5c;
    --ink:#3b3b3d;
    --text:#222222;
    --rule:#bdbdbd;
    --paper:#ffffff;
  }
  *{margin:0;padding:0;box-sizing:border-box}
  html,body{width:1200px;height:1200px;overflow:hidden}
  body{
    position:relative;
    font-family:"Inter",Helvetica,Arial,sans-serif;
    background:radial-gradient(ellipse at 50% 30%,#f0f0f0 0%,#dedede 45%,#b9b9b9 100%);
    color:var(--text);
  }
  .panel{position:absolute;background:var(--paper);overflow:hidden}
  .panel--narrow{left:68px;top:222px;width:226px;height:757px}
  .panel--wide{left:340px;top:224px;width:786px;height:756px}

  .size-label{position:absolute;top:995px;font-size:27px;font-weight:300;color:#1a1a1a;transform:translateX(-50%);white-space:nowrap}
  .size-label--narrow{left:181px}
  .size-label--wide{left:733px}

  .portrait{position:absolute;background:linear-gradient(160deg,#f6ede6 0%,#efd7c8 40%,#e5c2ad 70%,#f4ebe4 100%)}

  /* narrow panel */
  .panel--narrow .portrait{left:0;top:0;width:226px;height:405px}
  .gold-band{position:absolute;left:0;top:405px;width:226px;height:9px;background:var(--gold)}
  .gold-notch{position:absolute;left:101px;top:413px;width:0;height:0;border-left:12px solid transparent;border-right:12px solid transparent;border-top:9px solid var(--gold)}
  .narrow-title{position:absolute;left:0;top:430px;width:226px;text-align:center;font-size:33px;font-weight:300;color:var(--red);letter-spacing:-0.5px}
  .narrow-rule{position:absolute;left:65px;top:468px;width:96px;height:1px;background:var(--ink)}
  .narrow-sub{position:absolute;left:0;top:471px;width:226px;text-align:center;font-size:24px;font-weight:300;color:var(--gold);letter-spacing:-0.5px}
  .narrow-copy{position:absolute;left:19px;top:516px;width:186px;font-size:8.6px;line-height:11.5px;text-align:justify;text-align-last:left}
  .accent{color:var(--red)}

  .facts{position:absolute;display:flex;align-items:flex-start}
  .fact{display:flex;flex-direction:column;align-items:center;text-align:center;color:#333}
  .fact + .fact{border-left:1px solid var(--rule)}
  .facts--narrow{left:26px;top:603px}
  .facts--narrow .fact{width:43px;height:36px;font-size:5.4px;line-height:6px}
  .facts--narrow .fact svg{width:22px;height:22px;margin-bottom:3px}
  .facts--wide{left:463px;top:488px}
  .facts--wide .fact{width:80px;height:64px;font-size:10.5px;line-height:11px}
  .facts--wide .fact svg{width:40px;height:40px;margin-bottom:6px}

  .brand{position:absolute;display:flex;align-items:center;color:var(--ink);font-weight:800;letter-spacing:-1px}
  .brand-dot{border-radius:50%;border:3px solid var(--gold);flex:none}
  .panel--narrow .brand{left:24px;top:672px;font-size:31px;gap:8px}
  .panel--narrow .brand-dot{width:26px;height:26px;border-width:2.5px}

  .footer-band{position:absolute;left:0;bottom:0;width:100%;background:var(--gold);display:flex;align-items:center;justify-content:center;color:#fff;font-weight:300}
  .panel--narrow .footer-band{height:23px;font-size:12px;gap:6px}
  .panel--wide .footer-band{height:67px;font-size:31px;gap:14px}
  .social{border-radius:50%;background:#fff;flex:none}
  .panel--narrow .social{width:11px;height:11px}
  .panel--wide .social{width:28px;height:28px}
  .panel--wide .footer-band .url{margin-right:12px}
  .panel--narrow .footer-band .url{margin-right:4px}

  /* wide panel */
  .panel--wide .portrait{left:0;top:0;width:420px;height:689px}
  .panel--wide .brand{right:44px;top:52px;font-size:68px;gap:16px;letter-spacing:-2px}
  .panel--wide .brand-dot{width:64px;height:64px;border-width:5px}
  .wide-title{position:absolute;right:42px;top:202px;font-size:78px;font-weight:400;color:var(--red);letter-spacing:-1.5px}
  .wide-sub{position:absolute;right:42px;top:285px;font-size:45px;font-weight:300;color:var(--gold);letter-spacing:-0.5px}
  .wide-copy{position:absolute;left:463px;top:357px;width:280px;font-size:14.6px;line-height:18.2px;text-align:justify;text-align-last:left}
</style>
</head>
<body>

<section class="panel panel--narrow">
  <div class="portrait" role="img" aria-label="Photo of a woman with eyes closed, hands framing her face"></div>
  <div class="gold-band"></div>
  <div class="gold-notch"></div>
  <h2 class="narrow-title">ANTIAGING</h2>
  <div class="narrow-rule"></div>
  <p class="narrow-sub">Wrinkle Filling</p>
  <p class="narrow-copy">We offer mechanical treatments that stimulate your dermis, but also chemical treatments that awaken the hyaluronic acid and collagen present in your skin to give <span class="accent">your face, neck and chest a youthful look .</span></p>

  <div class="facts facts--narrow">
    <div class="fact">
      <svg viewBox="0 0 40 40"><g fill="#c8102e"><text x="1" y="13" font-size="12" font-weight="700" font-family="Inter,sans-serif">1</text><text x="1" y="25" font-size="12" font-weight="700" font-family="Inter,sans-serif">2</text><text x="1" y="37" font-size="12" font-weight="700" font-family="Inter,sans-serif">3</text><rect x="11" y="5" width="26" height="5"/><rect x="11" y="17" width="26" height="5"/><rect x="11" y="29" width="26" height="5"/></g></svg>
      1 session
    </div>
    <div class="fact">
      <svg viewBox="0 0 40 40"><g fill="none" stroke="#c8102e" stroke-width="2"><circle cx="23" cy="22" r="13"/><path d="M20 5h6M23 5v4M23 22l5-6M3 18h8M5 23h6M3 28h8"/></g></svg>
      +/- 45minutes
    </div>
    <div class="fact">
      <svg viewBox="0 0 40 40"><path d="M22 4h13v13L17 35 4 22z" fill="#c8102e"/><circle cx="30" cy="9" r="2.5" fill="#fff"/></svg>
      From 180 €
    </div>
    <div class="fact">
      <svg viewBox="0 0 40 40"><g fill="none" stroke="#c8102e" stroke-width="2.4"><path d="M9 12A14 14 0 1 1 6 22"/></g><path d="M4 6l2 10 9-4z" fill="#c8102e"/></svg>
      9 to 12<br>months
    </div>
  </div>

  <div class="brand"><span class="brand-dot"></span>Lumivora</div>

  <footer class="footer-band"><span class="url">www.lumivora.be</span><span class="social"></span><span class="social"></span></footer>
</section>

<section class="panel panel--wide">
  <div class="portrait" role="img" aria-label="Photo of a woman with eyes closed, hands framing her face"></div>
  <div class="brand"><span class="brand-dot"></span>Lumivora</div>
  <h2 class="wide-title">Antiaging</h2>
  <p class="wide-sub">Wrinkle Filling</p>
  <p class="wide-copy">We offer mechanical treatments that stimulate your dermis, but also chemical treatments that awaken the hyaluronic acid and collagen present in your skin to give <span class="accent">your face, neck and chest a youthful look .</span></p>

  <div class="facts facts--wide">
    <div class="fact">
      <svg viewBox="0 0 40 40"><g fill="#c8102e"><text x="1" y="13" font-size="12" font-weight="700" font-family="Inter,sans-serif">1</text><text x="1" y="25" font-size="12" font-weight="700" font-family="Inter,sans-serif">2</text><text x="1" y="37" font-size="12" font-weight="700" font-family="Inter,sans-serif">3</text><rect x="11" y="5" width="26" height="5"/><rect x="11" y="17" width="26" height="5"/><rect x="11" y="29" width="26" height="5"/></g></svg>
      1 session
    </div>
    <div class="fact">
      <svg viewBox="0 0 40 40"><g fill="none" stroke="#c8102e" stroke-width="2"><circle cx="23" cy="22" r="13"/><path d="M20 5h6M23 5v4M23 22l5-6M3 18h8M5 23h6M3 28h8"/></g></svg>
      +/- 45minutes
    </div>
    <div class="fact">
      <svg viewBox="0 0 40 40"><path d="M22 4h13v13L17 35 4 22z" fill="#c8102e"/><circle cx="30" cy="9" r="2.5" fill="#fff"/></svg>
      From 180 €
    </div>
    <div class="fact">
      <svg viewBox="0 0 40 40"><g fill="none" stroke="#c8102e" stroke-width="2.4"><path d="M9 12A14 14 0 1 1 6 22"/></g><path d="M4 6l2 10 9-4z" fill="#c8102e"/></svg>
      9 to 12<br>months
    </div>
  </div>

  <footer class="footer-band"><span class="url">www.lumivora.be</span><span class="social"></span><span class="social"></span></footer>
</section>

<p class="size-label size-label--narrow">134 cm x 40 cm</p>
<p class="size-label size-label--wide">125 cm x 130 cm</p>

</body>
</html>
```